Brightleaf Practice Partners, Inc (www.brightleafpracticepartnrs.example) would like to design a website to convey a level of professionalism to healthcare providers that we are the place form them to visit for Contin. Education, Marketing and Management, Joint Venture Partnerships, etc.
We think we would like a WP Site so that we can use the dynamic and static sides of it's capabilities. We also want to have something that acts as a membership side where members can post their Bio and CV's and prospective employers can post help wanted ads.

Target Market(s)

Pediatricians, Pediatric Dentist, Employers seeking these doctors

Industry/Entity Type

Healthcare

Requirements
Must have
• Services:
Resumes/Bio
Help Wanted
Continuing Education Programs
Marketing & Management

```html
<!DOCTYPE html>
<html lang="en">
<head>
<meta charset="utf-8">
<title>Brightleaf Practice Partners</title>
<link rel="stylesheet" href="https://fonts.googleapis.com/css2?family=Arimo:wght@400;700&family=Open+Sans:wght@400;600&display=swap">
<style>
:root{
  --header-teal:#5f9fb0;
  --header-line:#4d8c9e;
  --band-teal:#2e7a8e;
  --bar-top:#2a7fa2;
  --bar-bottom:#0f4b66;
  --title-blue:#1b6fa2;
  --page-bg:#eeeff0;
  --card-bg:#ffffff;
  --list-bg:#e7e8e9;
  --text-dark:#222;
  --text-mid:#555;
  --white:#fff;
}
*{margin:0;padding:0;box-sizing:border-box}
html,body{width:1084px;height:1200px;overflow:hidden}
body{position:relative;background:var(--page-bg);font-family:"Arimo",Arial,sans-serif;color:var(--text-dark)}
.abs{position:absolute}

.site-header{left:0;top:0;width:1084px;height:113px;background:
  repeating-linear-gradient(0deg,rgba(255,255,255,.06) 0 1px,transparent 1px 4px),
  repeating-linear-gradient(90deg,rgba(255,255,255,.06) 0 1px,transparent 1px 4px),
  linear-gradient(var(--header-teal),#4f8fa1);border-bottom:2px solid var(--header-line)}
.brand{left:44px;top:26px;color:var(--white);font-weight:700;font-size:22px;line-height:26px;display:flex;align-items:center;gap:10px}
.brand-dot{width:12px;height:12px;border-radius:50%;background:var(--white);flex:none}
.nav-home{left:367px;top:20px;width:63px;height:69px;background:linear-gradient(#1f6d82,#0f4c5e);border:2px solid #8fc1cf;display:flex;align-items:center;justify-content:center}
.nav-link{top:43px;color:#e9f3f6;text-decoration:none;font-size:16px;white-space:nowrap}
.nav-home .nav-link{position:static;color:var(--white)}

.hero-band{left:0;top:115px;width:1084px;height:311px;background:
  repeating-linear-gradient(0deg,rgba(255,255,255,.05) 0 1px,transparent 1px 4px),
  repeating-linear-gradient(90deg,rgba(255,255,255,.05) 0 1px,transparent 1px 4px),var(--band-teal)}
.hero-title{left:5px;top:234px;font-size:31px;font-weight:400;letter-spacing:1.5px;color:#0d2b33;white-space:nowrap}
.hero-copy{left:9px;top:298px;color:var(--white);font-size:12.5px;line-height:20px;white-space:nowrap}
.slider-dots{left:343px;top:390px;width:77px;height:24px;border-radius:6px;background:#e9ecee;display:flex;align-items:center;justify-content:center;gap:5px}
.slider-dots span{width:10px;height:10px;border-radius:50%;background:#8a8f93}
.slider-dots span.on{background:#b5441f}
.hero-photo{left:429px;top:149px;width:652px;height:434px;border:5px solid var(--white);background:linear-gradient(135deg,#d8dde3,#a9b3bb 50%,#7c6a5e);box-shadow:0 10px 14px -8px rgba(0,0,0,.45)}

.side-card{left:23px;top:503px;width:332px;height:488px;background:var(--card-bg);border:3px solid #dcdcdc;box-shadow:0 2px 4px rgba(0,0,0,.2)}
.side-photo{left:3px;top:3px;width:320px;height:141px;background:linear-gradient(120deg,#c8d4dc,#eef0f2 55%,#b9c6cf)}
.bar{background:linear-gradient(var(--bar-top),var(--bar-bottom));color:var(--white);font-size:15px;padding-left:10px;display:flex;align-items:center;border-bottom:3px solid #7fb2c8;white-space:nowrap}
.side-bar{left:-3px;top:144px;width:335px;height:40px}
.quotes{left:12px;top:200px;width:300px}
.quote{font-size:13px;line-height:20px;margin-bottom:9px;white-space:nowrap}
.quote cite{display:block;text-align:right;color:var(--text-mid);font-style:normal;padding-right:4px}

.welcome-title{left:436px;top:627px;font-size:20px;font-weight:400;color:var(--title-blue);white-space:nowrap}
.welcome-copy{left:434px;top:661px;font-size:12.5px;line-height:20px;color:var(--text-mid);white-space:nowrap}
.rule{left:428px;top:768px;width:650px;height:2px;background:linear-gradient(90deg,transparent,#9aa1a6 15%,#9aa1a6 85%,transparent)}

.info-box{top:801px;width:342px;height:190px;background:var(--list-bg);border:2px solid #d6d6d6;box-shadow:0 2px 4px rgba(0,0,0,.2);overflow:hidden}
.info-box .bar{position:absolute;left:-2px;top:-2px;width:344px;height:32px}
.info-photo{left:0;top:30px;width:165px;height:158px}
.info-list{left:170px;top:40px;list-style:none;font-size:12.5px;line-height:23.7px;color:var(--text-dark);white-space:nowrap}
.info-list li::before{content:"›";margin-right:11px;font-weight:700}
.read-more{right:14px;bottom:8px;color:var(--title-blue);font-size:13px}

.site-footer{left:0;top:1083px;width:1084px;height:117px;background:
  repeating-linear-gradient(0deg,rgba(255,255,255,.05) 0 1px,transparent 1px 4px),
  repeating-linear-gradient(90deg,rgba(255,255,255,.05) 0 1px,transparent 1px 4px),var(--band-teal)}
.follow-tab{left:376px;top:1057px;width:332px;height:54px;border-radius:10px;background:linear-gradient(#3b8aa0,#1d6477);border:3px solid #a7cfd9;display:flex;align-items:center;padding-left:30px;color:var(--white);font-size:23px;font-family:"Open Sans",Arial,sans-serif}
.social{width:32px;height:32px;border-radius:50%;background:#1f4f7a;border:2px solid #d9ecf2;margin-left:22px}
.social.second{background:#3b9bd2}
.footer-lines{left:0;top:1118px;width:1084px;text-align:center;color:#d8ecf1;font-size:13px;line-height:26px}
</style>
</head>
<body>
<header class="site-header abs">
  <div class="brand abs"><span class="brand-dot"></span><span>Brightleaf<br>Practice Partners</span></div>
  <nav>
    <div class="nav-home abs"><a class="nav-link" href="#">Home</a></div>
    <a class="nav-link abs" href="#" style="left:437px">About us</a>
    <a class="nav-link abs" href="#" style="left:521px">Education Programes</a>
    <a class="nav-link abs" href="#" style="left:696px">Marketing &amp; Managment</a>
    <a class="nav-link abs" href="#" style="left:893px">Memebers</a>
    <a class="nav-link abs" href="#" style="left:988px">Contact Us</a>
  </nav>
</header>

<section class="hero-band abs"></section>
<h1 class="hero-title abs">CONTIN. EDUCATION</h1>
<p class="hero-copy abs">Lorem Ipsum is simply dummy text of the printing and typeset-<br>ting industry. Lorem Ipsum has been the industry's standard<br>dummy text ever since the 1500s, when an unknown printer</p>
<div class="slider-dots abs"><span></span><span></span><span></span><span class="on"></span></div>
<div class="hero-photo abs" role="img" aria-label="Students in lab coats working and taking notes in a science lab"></div>

<aside class="side-card abs">
  <div class="side-photo abs" role="img" aria-label="Doctor with stethoscope in a hospital ward"></div>
  <div class="bar side-bar abs">Marketing &amp; Managment</div>
  <div class="quotes abs">
    <p class="quote">Lorem Ipsum is simply dummy text of the printing<br>and typesetting industry. Lorem has been the indus-<cite>-- Corwin</cite></p>
    <p class="quote">Lorem Ipsum is simply dummy text of the printing<br>and typesetting industry. Lorem has been the indus-<cite>-- Corwin</cite></p>
    <p class="quote">Lorem Ipsum is simply dummy text of the printing<br>and typesetting industry. Lorem has been the indus-<cite>-- Corwin</cite></p>
    <p class="quote">Lorem Ipsum is simply dummy text of the printing<br>and typesetting industry. Lorem has been the indus-<cite>-- Corwin</cite></p>
  </div>
</aside>

<h2 class="welcome-title abs">Welcome to Brightleaf Practice Partners</h2>
<p class="welcome-copy abs">Lorem Ipsum is simply dummy text of the printing and typesetting industry. Lorem Ipsum has been the indus-<br>try's standard dummy text ever since the 1500s, when an unknown printer took a galley of type and scrambled<br>it to make a type specimen book. It has survived not only five centuries, but also the leap into electronic type-<br>setting, remaining essentially unchanged. It was popularised in the 1960s with the release of Letraset sheets</p>
<div class="rule abs"></div>

<section class="info-box abs" style="left:379px">
  <div class="bar">Continuing Education Programe</div>
  <div class="info-photo abs" role="img" aria-label="Nurse in scrubs holding books" style="background:linear-gradient(135deg,#f4f5f6,#c9d7e3 60%,#8fa9c2)"></div>
  <ul class="info-list abs">
    <li>Lorem Ipsum is simply</li><li>Lorem Ipsum is simply</li><li>Lorem Ipsum is simply</li><li>Lorem Ipsum is simply</li><li>Lorem Ipsum is simply</li>
  </ul>
  <a class="read-more abs">Read More</a>
</section>

<section class="info-box abs" style="left:739px">
  <div class="bar">Services</div>
  <div class="info-photo abs" role="img" aria-label="Medical team reviewing a chart together" style="width:157px;background:linear-gradient(135deg,#eef1f3,#cfd9e0 55%,#9fb3c2)"></div>
  <ul class="info-list abs" style="left:163px">
    <li>Lorem Ipsum is simply is a</li><li>Lorem Ipsum is simply is a</li><li>Lorem Ipsum is simply is a</li><li>Lorem Ipsum is simply &nbsp;is a</li><li>Lorem Ipsum is simply &nbsp;is a</li>
  </ul>
  <a class="read-more abs">Read More</a>
</section>

<footer class="site-footer abs"></footer>
<div class="follow-tab abs">Follow us on<span class="social"></span><span class="social second"></span></div>
<div class="footer-lines abs">
  <p>Brightleaf Practice Partners</p>
  <p>About Us | Find a Pediatrician | Locations | Office Hours | Contact</p>
  <p>Copyright © 2011 Brightleaf Practice Partners</p>
</div>
</body>
</html>
```